Flyer for a Business Consultant

I need a one-page description of services. I am a Brinmore Accredited Talents Mentor. I do not have a personal website but think I will soon purchase this template https://quillerlayouts.example/layouts/lectern/. I like the larger font, simplicity and larger font. I will attach his pricing flyer which I like - not to overly guide or restrict your creative thinking, but only to give a little perspective. I don't like busy, noisy - I like clarity, simplicity. Here 's the Brinmore website which these same traits https://www.brinmoretalentshub.example/ and can be a source of ideas and colors.

Target Market(s)

CEOs and Middle Managers in organizations

Industry/Entity Type

Financial Service

Colors

Designer to choose colors to be used in the design.

Requirements
Must have
• Clarity, simplicity, but also strength (not weak or frilly looking)
Nice to have
• Warm color(s), larger/not skinny font
Should not have
• Loud, noisy, busy

```html
<!DOCTYPE html>
<html lang="en">
<head>
<meta charset="utf-8">
<title>Strength-Based Team Effectiveness Flyer</title>
<link href="https://fonts.googleapis.com/css2?family=Open+Sans:ital,wght@0,300;0,400;0,600;0,700;0,800;1,400&family=Bebas+Neue&display=swap" rel="stylesheet">
<style>
  :root {
    --bg: #5b5d5c;
    --paper: #ffffff;
    --ink: #231f20;
    --body-ink: #2b2b2b;
    --red: #d1202f;
    --orange-1: #f7941d;
    --orange-2: #f37321;
    --orange-3: #ef5525;
    --pill-top: #fbb040;
    --pill-bottom: #f47b20;
    --muted: #555555;
    --rule: #333333;
    --badge-grey: #8a8a8a;
  }
  * { box-sizing: border-box; margin: 0; padding: 0; }
  html, body { width: 975px; height: 1200px; overflow: hidden; }
  body { background: var(--bg); font-family: "Open Sans", Arial, sans-serif; position: relative; }

  .flyer { position: absolute; left: 83px; top: 75px; width: 809px; height: 1047px; background: var(--paper); overflow: hidden; }

  .photo-backdrop {
    position: absolute; left: 0; top: 470px; width: 809px; height: 577px;
    background: radial-gradient(ellipse at 70% 30%, #e4e4e4 0%, #f1f1f1 45%, #ffffff 80%),
                linear-gradient(180deg, #ffffff 0%, #ececec 40%, #f4f4f4 100%);
    opacity: .85;
  }

  .headline { position: absolute; top: 62px; left: 0; width: 100%; text-align: center; color: var(--ink); }
  .headline .lead { display: block; font-weight: 300; font-size: 31px; letter-spacing: .2px; line-height: 38px; }
  .headline .main { display: block; font-weight: 800; font-size: 40px; letter-spacing: .5px; line-height: 44px; }

  .grow-title { position: absolute; top: 162px; width: 100%; text-align: center; color: var(--red); font-weight: 700; font-size: 20px; letter-spacing: .3px; }

  .benefits { position: absolute; left: 110px; top: 202px; width: 625px; height: 238px; }
  .benefits svg { position: absolute; inset: 0; }
  .benefit-text { position: absolute; top: 24px; color: #fff; font-family: "Bebas Neue", "Arial Narrow", sans-serif; font-size: 23px; line-height: 25px; letter-spacing: .3px; }
  .benefit-1 { left: 20px; width: 170px; }
  .benefit-2 { left: 230px; width: 150px; top: 30px; }
  .benefit-3 { left: 427px; width: 150px; top: 34px; }

  .service { position: absolute; left: 0; width: 100%; text-align: center; }
  .pill {
    display: block; margin: 0 auto; width: 386px; height: 33px; border-radius: 12px;
    background: linear-gradient(180deg, var(--pill-top) 0%, var(--pill-bottom) 100%);
    color: #fff; font-weight: 700; font-size: 18px; line-height: 33px; letter-spacing: .3px;
  }
  .service p { margin: 8px auto 0; width: 560px; color: var(--body-ink); font-weight: 600; font-size: 13.6px; line-height: 21px; }
  .service.individual { top: 472px; }
  .service.workshop { top: 621px; }
  .service.follow-on { top: 766px; }
  .service.follow-on p { width: 620px; }

  .credential { position: absolute; left: 39px; top: 955px; width: 248px; height: 67px; background: #fff; border: 1px solid #c9c9c9; display: flex; align-items: center; gap: 10px; padding: 0 12px; }
  .credential .mark { width: 36px; height: 42px; background: var(--badge-grey); border-radius: 3px; flex: none; }
  .credential .label { color: #6d6d6d; font-size: 14px; line-height: 17px; font-weight: 400; }

  .contact-name { position: absolute; left: 305px; top: 968px; width: 240px; text-align: center; }
  .contact-name .name { display: block; color: var(--red); font-weight: 700; font-size: 20px; line-height: 26px; }
  .contact-name .role { display: block; color: var(--muted); font-style: italic; font-size: 10.5px; line-height: 14px; }
  .divider { position: absolute; left: 551px; top: 965px; width: 1px; height: 42px; background: var(--rule); }
  .contact-lines { position: absolute; left: 572px; top: 968px; color: var(--ink); }
  .contact-lines .line { display: flex; align-items: center; gap: 10px; }
  .contact-lines .phone { font-size: 20px; line-height: 26px; }
  .contact-lines .email { font-size: 12.5px; font-weight: 700; line-height: 20px; }
  .contact-lines svg { flex: none; }
</style>
</head>
<body>
  <main class="flyer">
    <div class="photo-backdrop" role="img" aria-label="Faded photograph of a smiling business team joining hands"></div>

    <h1 class="headline">
      <span class="lead">A STRENGTH-BASED APPROACH TO</span>
      <span class="main">MANAGING TEAM EFFECTIVENESS</span>
    </h1>

    <h2 class="grow-title">WE HELP TEAMS GROW STRONGER BY</h2>

    <section class="benefits">
      <svg width="625" height="238" viewBox="0 0 625 238" aria-hidden="true">
        <polygon points="390,0 585,0 585,143 625,191 585,238 390,238" fill="var(--orange-3)"/>
        <polygon points="195,0 390,0 390,143 430,191 390,238 195,238" fill="var(--orange-2)"/>
        <polygon points="0,0 195,0 195,143 235,191 195,238 0,238" fill="var(--orange-1)"/>
        <!-- partnership icon -->
        <g fill="#fff">
          <circle cx="152" cy="178" r="7"/>
          <rect x="143" y="187" width="18" height="24" rx="4"/>
          <circle cx="178" cy="178" r="7"/>
          <rect x="169" y="187" width="18" height="24" rx="4"/>
          <rect x="155" y="192" width="20" height="5" rx="2"/>
        </g>
        <!-- conversation icon -->
        <g fill="#fff">
          <rect x="150" y="0" width="0" height="0"/>
          <rect x="340" y="157" width="24" height="14" rx="5" transform="translate(-150 0)"/>
          <polygon points="196,170 200,177 204,170"/>
          <circle cx="186" cy="183" r="0"/>
          <circle cx="345" cy="186" r="6"/>
          <rect x="336" y="194" width="18" height="17" rx="4"/>
          <circle cx="370" cy="186" r="6"/>
          <rect x="361" y="194" width="18" height="17" rx="4"/>
        </g>
        <g fill="var(--orange-2)">
          <circle cx="196" cy="164" r="1.6"/><circle cx="202" cy="164" r="1.6"/><circle cx="208" cy="164" r="1.6"/>
        </g>
        <!-- team icon -->
        <g fill="#fff">
          <circle cx="536" cy="178" r="6"/>
          <rect x="528" y="186" width="16" height="24" rx="3"/>
          <circle cx="552" cy="175" r="7"/>
          <rect x="543" y="184" width="18" height="29" rx="3"/>
          <circle cx="568" cy="178" r="6"/>
          <rect x="560" y="186" width="16" height="24" rx="3"/>
        </g>
      </svg>
      <p class="benefit-text benefit-1">Bringing a deep awareness of their strengths and the strengths of their associates.</p>
      <p class="benefit-text benefit-2">Increasing the team’s communication and sense of partnership.</p>
      <p class="benefit-text benefit-3">Improving employee engagement and effectiveness.</p>
    </section>

    <section class="service individual">
      <h3 class="pill">INDIVIDUAL SESSIONS</h3>
      <p>Conversational feedback and coaching sessions based on Brinmore’s TalentCompass assessments. These sessions last about an hour and lead to a personalized translation of the results and how their strengths show up in their work and inherent blind spots they bring.</p>
    </section>

    <section class="service workshop">
      <h3 class="pill">STRENGTH DISCOVERY WORKSHOP</h3>
      <p>A retreat-style Team Workshop in which the team learns each other’s unique Top 5 strengths. The session is very interactive and provides a common language that leads to improved communication and effectiveness. Tailored in 2.3.and 4-hour options are tailored to your Team’s challenges and opportunities.</p>
    </section>

    <section class="service follow-on">
      <h3 class="pill">FOLLOW-ON MODULES</h3>
      <p>Follow-on is important to make the insights learned to be practical and integrated into the Teams’ approach and workflows.<br>In a debrief session included as part of the workshop, we provide several 15-minute exercise modules for use in regular meetings, and we offer guest facilitated modules of 30- 60 minutes each.</p>
    </section>

    <div class="credential">
      <span class="mark"></span>
      <span class="label">Brinmore Accredited Talents Mentor</span>
    </div>

    <div class="contact-name">
      <span class="name">Warren Calloway</span>
      <span class="role">Brinmore Workplace Talents Mentor</span>
    </div>
    <div class="divider"></div>
    <div class="contact-lines">
      <div class="line phone">
        <svg width="14" height="12" viewBox="0 0 14 12" aria-hidden="true"><path d="M1 4 Q7 -1 13 4 L11 5.5 L9.5 4 L4.5 4 L3 5.5 Z M3 6 L11 6 L12 11 L2 11 Z" fill="var(--red)"/></svg>
        <span>615-555-0147</span>
      </div>
      <div class="line email">
        <svg width="14" height="12" viewBox="0 0 14 12" aria-hidden="true"><rect x="0.5" y="1.5" width="13" height="9" rx="1" fill="var(--red)"/><polyline points="1,2 7,7 13,2" fill="none" stroke="#fff" stroke-width="1.2"/></svg>
        <span>warren@talentsforge.example</span>
      </div>
    </div>
  </main>
</body>
</html>
```